TALMORK

The business want a professional looking business card. We have a scetch we will add but want the extra upgrade, and would like more suggestions for variations of our business cards.

```html
<!DOCTYPE html>
<html lang="en">
<head>
<meta charset="utf-8">
<title>TALMORK – Business Card</title>
<link href="https://fonts.googleapis.com/css2?family=Cinzel:wght@600&family=Source+Sans+3:wght@400&display=swap" rel="stylesheet">
<style>
  :root {
    --backdrop: #bdbdbf;
    --card: #000000;
    --gold: #e6c77f;
    --gold-light: #f3d993;
    --text-gold: #f0d594;
  }
  * { margin: 0; padding: 0; box-sizing: border-box; }
  html, body { width: 1200px; height: 960px; overflow: hidden; }
  body { background: var(--backdrop); position: relative; }

  .card { position: absolute; background: var(--card); overflow: hidden; }
  .card--front { left: 140px; top: 38px; width: 765px; height: 437px; }
  .card--back  { left: 291px; top: 504px; width: 765px; height: 437px; }

  .accent-bar {
    position: absolute; left: 0; top: 198px; width: 25px; height: 239px;
    background: var(--gold-light);
  }

  .brand-name {
    position: absolute; font-family: "Cinzel", serif; font-weight: 600;
    color: var(--gold); letter-spacing: 1px; white-space: nowrap;
  }
  .card--front .brand-name { left: 510px; top: 148px; width: 200px; text-align: center; font-size: 34px; }
  .card--back .brand-name { left: 0; width: 100%; top: 236px; text-align: center; font-size: 56px; letter-spacing: 2px; }

  .brand-dot {
    position: absolute; border-radius: 50%; background: var(--gold);
  }
  .card--back .brand-dot { left: 343px; top: 120px; width: 80px; height: 80px; }

  .holder { position: absolute; left: 46px; top: 204px; }
  .holder__name {
    font-family: "Cinzel", serif; font-weight: 600; font-size: 31px;
    color: var(--text-gold); letter-spacing: 0.5px; white-space: nowrap; line-height: 1;
  }
  .holder__role, .holder__person {
    font-family: "Source Sans 3", sans-serif; font-size: 19px; color: var(--text-gold);
    line-height: 28px;
  }
  .holder__role { margin-top: 22px; }

  .divider {
    position: absolute; left: 46px; top: 313px; width: 387px; height: 2px;
    background: var(--gold-light);
  }

  .contacts { position: absolute; left: 46px; top: 326px; list-style: none; }
  .contacts__item {
    display: flex; align-items: center; height: 25.5px;
    font-family: "Source Sans 3", sans-serif; font-size: 19px; color: var(--text-gold);
  }
  .contacts__icon { width: 17px; height: 17px; margin-right: 19px; fill: var(--gold-light); }
</style>
</head>
<body>

<section class="card card--front">
  <div class="accent-bar"></div>

  <div class="brand-name">TALMORK</div>

  <div class="holder">
    <div class="holder__name">TALMORK HALVORSEN</div>
    <div class="holder__role">CEO &amp; FOUNDER</div>
    <div class="holder__person">ERIK ANDERS HALVORSEN</div>
  </div>

  <div class="divider"></div>

  <ul class="contacts">
    <li class="contacts__item">
      <svg class="contacts__icon" viewBox="0 0 24 24" aria-hidden="true"><path d="M6.6 10.8a15.1 15.1 0 0 0 6.6 6.6l2.2-2.2c.3-.3.7-.4 1-.2 1.1.4 2.3.6 3.6.6.6 0 1 .4 1 1V20c0 .6-.4 1-1 1A17 17 0 0 1 3 4c0-.6.4-1 1-1h3.5c.6 0 1 .4 1 1 0 1.3.2 2.5.6 3.6.1.3 0 .7-.2 1z"/></svg>
      004791234567
    </li>
    <li class="contacts__item">
      <svg class="contacts__icon" viewBox="0 0 24 24" aria-hidden="true"><path d="M2 9l10-7 10 7v12H2z M4 10.5v.3l8 5.5 8-5.5v-.3l-8 5.4z" fill-rule="evenodd"/></svg>
      talmork.llc@example.com
    </li>
    <li class="contacts__item">
      <svg class="contacts__icon" viewBox="0 0 24 24" aria-hidden="true"><path d="M12 2a10 10 0 1 0 0 20 10 10 0 0 0 0-20zm-1 2.1V8H7.6A8 8 0 0 1 11 4.1zm2 0A8 8 0 0 1 16.4 8H13zM5 10h6v4H5a8 8 0 0 1 0-4zm8 0h6a8 8 0 0 1 0 4h-6zm-5.4 6H11v3.9A8 8 0 0 1 7.6 16zm5.4 0h3.4a8 8 0 0 1-3.4 3.9z"/></svg>
      www.talmork.llc
    </li>
  </ul>
</section>

<section class="card card--back">
  <div class="brand-dot"></div>
  <div class="brand-name">TALMORK</div>
</section>

</body>
</html>
```